loyalty card design needed

Inner city Coffee shop/cafe- we need a loyalty card that will stand out in wallets.
Ideally we are wanting up to 4 rows of 10 sign boxes.

needs a note on it to say tenth coffee is free.

Target Market(s)

business people

Industry/Entity Type

Cafe

Contact Information for Business Card

LANTERN ROAST
47 Penrose Street
HOBART TASMANIA 7000
phone 03 61958342
www.lanternroast.com.au

Logo Text

LANTERN ROAST

Logo styles of interest
Wordmark Logo
Requirements
Must have
• Ideally we are wanting up to 4 rows of 10 sign boxes.

needs a note on it to say tenth coffee is free

colours as suggested in file upload
Nice to have
• really stand out form the rest of cards in a customers wallet.

```html
<!DOCTYPE html>
<html lang="en">
<head>
<meta charset="utf-8">
<title>Lantern Roast Loyalty Card</title>
<link rel="stylesheet" href="https://fonts.googleapis.com/css2?family=Archivo+Black&family=Arimo:wght@400;700&family=Kaushan+Script&display=swap">
<style>
  :root {
    --lime: #cfdc3a;
    --lime-deep: #b5c42a;
    --ink: #111111;
    --red: #d3202a;
    --paper: #ffffff;
    --backdrop: #e6e6e2;
  }
  * { box-sizing: border-box; margin: 0; padding: 0; }
  html, body { width: 1200px; height: 1200px; overflow: hidden; }
  body {
    background: var(--backdrop);
    font-family: "Arimo", Arial, sans-serif;
    color: var(--ink);
    position: relative;
  }
  .card {
    position: absolute;
    left: 150px;
    width: 900px;
    height: 500px;
    background: var(--lime);
    overflow: hidden;
    box-shadow: 0 6px 18px rgba(0,0,0,0.18);
  }
  .card--stamps { top: 60px; }
  .card--cover { top: 640px; }

  .stamp-panel { position: absolute; inset: 0; }

  .brand-title {
    position: absolute;
    font-family: "Archivo Black", "Arial Black", sans-serif;
    letter-spacing: 1px;
    line-height: 1;
  }
  .brand-title::after {
    content: "";
    position: absolute;
    left: 0; right: 0;
    bottom: -10px;
    height: 4px;
    background: var(--red);
  }
  .card--stamps .brand-title { top: 34px; right: 50px; font-size: 40px; }

  .stamp-grid {
    position: absolute;
    top: 120px;
    right: 52px;
    display: grid;
    grid-template-columns: repeat(5, 50px);
    grid-auto-rows: 50px;
    gap: 22px 26px;
  }
  .stamp-box {
    border: 4px solid var(--lime-deep);
    border-radius: 8px;
    background: var(--paper);
  }
  .stamp-box--free {
    background: var(--ink);
    border-color: var(--ink);
    display: flex;
    align-items: center;
    justify-content: center;
  }

  .free-note {
    position: absolute;
    left: 48px;
    top: 120px;
    width: 150px;
    height: 150px;
    border: 5px solid var(--red);
    border-radius: 50%;
    display: flex;
    flex-direction: column;
    align-items: center;
    justify-content: center;
    color: var(--red);
    font-family: "Archivo Black", "Arial Black", sans-serif;
    text-align: center;
    line-height: 1.05;
    background: var(--paper);
  }
  .free-note__small { font-size: 20px; }
  .free-note__big { font-size: 36px; }

  .contact-line {
    position: absolute;
    left: 56px;
    display: flex;
    align-items: flex-start;
    gap: 10px;
    font-size: 20px;
  }
  .contact-line--phone { top: 300px; }
  .contact-line--address { top: 360px; line-height: 1.25; }

  .web-address {
    position: absolute;
    font-weight: 700;
    font-size: 22px;
  }
  .card--stamps .web-address { right: 50px; bottom: 24px; }

  .card--cover .brand-title { top: 150px; left: 0; right: 0; margin: 0 auto; width: max-content; font-size: 60px; }
  .loyalty-label {
    position: absolute;
    top: 245px;
    left: 0; right: 0;
    text-align: center;
    font-family: "Kaushan Script", cursive;
    font-size: 58px;
  }
  .card--cover .web-address { left: 0; right: 0; bottom: 60px; text-align: center; }
</style>
</head>
<body>

<section class="card card--stamps" aria-label="Loyalty card, stamp side">
  <svg class="stamp-panel" viewBox="0 0 900 500" width="900" height="500" aria-hidden="true">
    <polygon points="210,0 900,0 900,420 350,450" fill="#ffffff"/>
  </svg>

  <h1 class="brand-title">LANTERN ROAST</h1>

  <div class="free-note">
    <span class="free-note__small">10th Coffee</span>
    <span class="free-note__small">is</span>
    <span class="free-note__big">FREE</span>
  </div>

  <div class="stamp-grid">
    <div class="stamp-box"></div><div class="stamp-box"></div><div class="stamp-box"></div><div class="stamp-box"></div>
    <div class="stamp-box stamp-box--free"><svg width="28" height="26" viewBox="0 0 28 26"><path d="M3 6h17v9a7 7 0 0 1-7 7h-3a7 7 0 0 1-7-7z" fill="#fff"/><path d="M20 9h3a3 3 0 0 1 0 6h-3" fill="none" stroke="#fff" stroke-width="2.5"/></svg></div>
    <div class="stamp-box"></div><div class="stamp-box"></div><div class="stamp-box"></div><div class="stamp-box"></div>
    <div class="stamp-box stamp-box--free"><svg width="28" height="26" viewBox="0 0 28 26"><path d="M3 6h17v9a7 7 0 0 1-7 7h-3a7 7 0 0 1-7-7z" fill="#fff"/><path d="M20 9h3a3 3 0 0 1 0 6h-3" fill="none" stroke="#fff" stroke-width="2.5"/></svg></div>
    <div class="stamp-box"></div><div class="stamp-box"></div><div class="stamp-box"></div><div class="stamp-box"></div>
    <div class="stamp-box stamp-box--free"><svg width="28" height="26" viewBox="0 0 28 26"><path d="M3 6h17v9a7 7 0 0 1-7 7h-3a7 7 0 0 1-7-7z" fill="#fff"/><path d="M20 9h3a3 3 0 0 1 0 6h-3" fill="none" stroke="#fff" stroke-width="2.5"/></svg></div>
    <div class="stamp-box"></div><div class="stamp-box"></div><div class="stamp-box"></div><div class="stamp-box"></div>
    <div class="stamp-box stamp-box--free"><svg width="28" height="26" viewBox="0 0 28 26"><path d="M3 6h17v9a7 7 0 0 1-7 7h-3a7 7 0 0 1-7-7z" fill="#fff"/><path d="M20 9h3a3 3 0 0 1 0 6h-3" fill="none" stroke="#fff" stroke-width="2.5"/></svg></div>
  </div>

  <p class="contact-line contact-line--phone">
    <svg width="20" height="20" viewBox="0 0 24 24" aria-hidden="true"><path d="M6.6 10.8a15 15 0 0 0 6.6 6.6l2.2-2.2a1 1 0 0 1 1-.25 11.4 11.4 0 0 0 3.6.57 1 1 0 0 1 1 1V20a1 1 0 0 1-1 1A17 17 0 0 1 3 4a1 1 0 0 1 1-1h3.5a1 1 0 0 1 1 1c0 1.25.2 2.45.57 3.57a1 1 0 0 1-.25 1z" fill="#d3202a"/></svg>
    <span>03 61958342</span>
  </p>
  <p class="contact-line contact-line--address">
    <svg width="20" height="20" viewBox="0 0 24 24" aria-hidden="true"><path d="M12 3 2 12h3v8h5v-5h4v5h5v-8h3z" fill="#d3202a"/></svg>
    <span>47 Penrose Street<br>HOBART TASMANIA<br>7000</span>
  </p>

  <p class="web-address">www.lanternroast.com.au</p>
</section>

<section class="card card--cover" aria-label="Loyalty card, cover side">
  <h2 class="brand-title">LANTERN ROAST</h2>
  <p class="loyalty-label">Loyalty Card</p>
  <p class="web-address">www.lanternroast.com.au</p>
</section>

</body>
</html>
```